Accounting business needs a great flyer

I need a flyer for my new business "Bright Ledger". I am an individual accountant working for himself on the Sunshine Coast in Queensland Australia. I would like to see designs that communicate reliability and trust. I believe my point of difference is that I am always available to my clients and I will cap my number of clients to ensure I can service them properly.
The main point I want to convey is that most of the time junior employees with little to no experience or unqualified employees do the tax work for the clients and a senior accountant quickly checks the work at the end but never gets to really know the clients business. Accountants in general seem to have a bad reputation for not responding to clients in a timely fashion, whether by email or phone. This is where I intend to differentiate myself. . I have also included some logo's that should go on the flyer.

Target Market(s)

Every small business

Industry/Entity Type

Public Accounting

Requirements
Must have
• Web address: www.brightledger.com.au
Phone number: 0418 592 637
Attached logos
Reference to: "Do you know who is actually doing your tax?"
Other accounting firms - use junior unqualified staff
- outsource to cheap labour countries
- use tax consultants who sometimes have had only 2 weeks training.
At Bright Ledger, a highly qualified CPA with a Masters in Taxation does your work from start to finish.
**I don't need it to say exactly this but I want the theme of the flyer to have these points in it.
Nice to have
• Something different

```html
<!DOCTYPE html>
<html lang="en">
<head>
<meta charset="utf-8">
<title>Bright Ledger – Individual &amp; Small Business Accounting Flyer</title>
<link href="https://fonts.googleapis.com/css2?family=Montserrat:wght@400;500;600;700;800&display=swap" rel="stylesheet">
<style>
  :root {
    --navy: #24316e;
    --navy-deep: #1d2860;
    --gold: #f2b418;
    --paper: #f6f6f3;
    --backdrop: #9b9a9c;
    --ink-light: #ffffff;
    --photo-warm: #b9a48e;
    --photo-cool: #6e6a66;
    --photo-dark: #8a7b6e;
    --badge-sky: #2bb3e3;
    --badge-olive: #c9cc8e;
    --badge-blue: #1558a8;
  }
  * { margin: 0; padding: 0; box-sizing: border-box; }
  html, body { width: 1200px; height: 800px; overflow: hidden; }
  body {
    background: var(--backdrop);
    font-family: "Montserrat", sans-serif;
    position: relative;
  }
  .flyer {
    position: absolute;
    left: 340px; top: 32px;
    width: 520px; height: 736px;
    background: var(--paper);
    overflow: hidden;
    box-shadow: 0 10px 30px rgba(0,0,0,.25);
  }
  .flyer-shapes { position: absolute; inset: 0; width: 520px; height: 736px; }
  .headline {
    position: absolute; left: 28px; top: 46px;
    text-transform: uppercase; line-height: 1.15;
  }
  .headline-main { display: block; color: var(--ink-light); font-weight: 800; font-size: 31px; letter-spacing: .5px; }
  .headline-sub { display: block; color: var(--gold); font-weight: 600; font-size: 27.5px; letter-spacing: .3px; }

  .reference { position: absolute; left: 30px; top: 320px; width: 300px; color: var(--navy); }
  .reference-title { font-size: 25px; font-weight: 800; letter-spacing: .5px; line-height: 1.2; }
  .reference-question { margin-top: 2px; color: var(--gold); font-size: 12px; font-weight: 500; white-space: nowrap; }
  .concern-list { list-style: none; margin-top: 8px; }
  .concern-list li {
    position: relative; padding-left: 24px; margin-bottom: 4px;
    font-size: 12.5px; font-weight: 600; line-height: 1.3;
  }
  .concern-icon { position: absolute; left: 0; top: 1px; width: 16px; height: 16px; }

  .promise {
    position: absolute; left: 0; top: 474px; width: 338px; height: 68px;
    background: var(--navy); border-radius: 0 34px 34px 0;
    padding: 10px 24px 0 30px;
    color: var(--ink-light); font-size: 13px; font-weight: 500; line-height: 1.35;
  }
  .availability {
    position: absolute; left: 30px; top: 554px; width: 320px;
    color: var(--navy); font-size: 13px; font-weight: 500; line-height: 1.4;
  }

  .brand { position: absolute; left: 370px; top: 322px; width: 140px; text-align: center; color: var(--ink-light); }
  .brand-mark { display: block; width: 46px; height: 46px; margin: 0 auto 10px; border: 2px solid var(--ink-light); border-radius: 50%; }
  .brand-name { font-size: 13px; font-weight: 500; letter-spacing: 4px; text-transform: uppercase; }

  .partner-badge { position: absolute; }
  .partner-badge.is-software { left: 452px; top: 426px; width: 38px; height: 38px; border-radius: 50%; background: var(--badge-sky); }
  .partner-badge.is-registry { left: 454px; top: 490px; width: 30px; height: 30px; border-radius: 50%; background: var(--badge-olive); border: 2px solid #f4f4ec; }
  .partner-badge.is-professional { left: 372px; top: 566px; width: 78px; height: 38px; background: var(--badge-blue); border-right: 26px solid var(--gold); }

  .contact { position: absolute; left: 300px; top: 682px; color: var(--navy); font-style: normal; }
  .contact-line { display: flex; align-items: center; gap: 10px; margin-bottom: 4px; }
  .contact-icon { width: 20px; height: 20px; flex: none; }
  .contact-phone { font-size: 17px; font-weight: 600; }
  .contact-web { font-size: 12.5px; font-weight: 600; }
</style>
</head>
<body>
<main class="flyer">
  <svg class="flyer-shapes" viewBox="0 0 520 736">
    <defs>
      <linearGradient id="photoTone" x1="0" y1="0" x2="1" y2="1">
        <stop offset="0" stop-color="var(--photo-dark)"/>
        <stop offset=".5" stop-color="var(--photo-warm)"/>
        <stop offset="1" stop-color="var(--photo-cool)"/>
      </linearGradient>
    </defs>
    <path class="side-panel" d="M310 300 L470 592 H520 V150 Z" fill="var(--navy-deep)"/>
    <path class="arc-gold" d="M0 0 H520 V170 C505 240 400 306 220 306 C120 306 50 285 0 262 Z" fill="var(--gold)"/>
    <path class="arc-navy" d="M0 0 H520 V120 C500 220 390 282 220 282 C120 282 50 262 0 240 Z" fill="var(--navy)"/>
    <path role="img" aria-label="Photo of an accountant meeting with clients around an office desk with a laptop"
          d="M0 0 H520 V60 C490 200 380 250 220 250 C120 250 50 230 0 210 Z" fill="url(#photoTone)"/>
    <path class="wave-navy" d="M0 618 C120 652 300 640 520 606 V630 C300 666 120 678 0 648 Z" fill="var(--navy)"/>
    <path class="wave-gold" d="M0 640 C120 672 300 660 520 622 V736 H0 Z" fill="var(--gold)"/>
    <path class="wave-paper" d="M0 648 C120 678 300 666 520 630 V648 C330 676 150 700 0 676 Z" fill="var(--paper)"/>
  </svg>

  <h1 class="headline">
    <span class="headline-main">Individual &amp; Small</span>
    <span class="headline-sub">Business Accounting</span>
  </h1>

  <section class="reference">
    <h2 class="reference-title">REFERENCE TO:</h2>
    <p class="reference-question">"Do you know who is actually doing your tax?"</p>
    <ul class="concern-list">
      <li>
        <svg class="concern-icon" viewBox="0 0 16 16"><circle cx="8" cy="8" r="8" fill="var(--gold)"/><path d="M4.5 8.3 7 10.6 11.6 5.6" stroke="#fff" stroke-width="1.8" fill="none"/></svg>
        Other Accounting Firms -<br>Use Junior Unqualified Staff
      </li>
      <li>
        <svg class="concern-icon" viewBox="0 0 16 16"><circle cx="8" cy="8" r="8" fill="var(--gold)"/><circle cx="8" cy="6" r="2.3" fill="#fff"/><path d="M4 12.5c.6-2.3 2.2-3.4 4-3.4s3.4 1.1 4 3.4z" fill="#fff"/></svg>
        Outsource To Cheap Labour Countries
      </li>
      <li>
        <svg class="concern-icon" viewBox="0 0 16 16"><circle cx="8" cy="8" r="8" fill="var(--gold)"/><circle cx="8" cy="8" r="4.6" stroke="#fff" stroke-width="1.4" fill="none"/><path d="M8 5.2V8h2.3" stroke="#fff" stroke-width="1.4" fill="none"/></svg>
        Use Tax Consultants Who Sometimes<br>Have Had Only 2Weeks Training.
      </li>
    </ul>
  </section>

  <p class="promise">At Bright Ledger, a highly qualified CPA with a Masters in Taxation does your work from start to finish.</p>

  <p class="availability">Always available to you by phone or email, with a capped client list so every business gets proper care.</p>

  <div class="brand">
    <span class="brand-mark"></span>
    <span class="brand-name">Bright Ledger</span>
  </div>

  <span class="partner-badge is-software"></span>
  <span class="partner-badge is-registry"></span>
  <span class="partner-badge is-professional"></span>

  <address class="contact">
    <p class="contact-line">
      <svg class="contact-icon" viewBox="0 0 20 20"><circle cx="10" cy="10" r="10" fill="var(--navy)"/><path d="M7 5.5c.5-.4 1-.3 1.3.2l.9 1.6c.2.4.1.8-.2 1.1l-.6.5c.5 1.2 1.4 2.1 2.6 2.7l.5-.6c.3-.3.7-.4 1.1-.2l1.6.9c.5.3.6.8.2 1.3-.8 1-2 1.3-3.2.7-2.2-1.1-3.900-2.8-4.900-5-.5-1.2-.2-2.4.7-3.2z" fill="#fff"/></svg>
      <span class="contact-phone">0418 592 637</span>
    </p>
    <p class="contact-line">
      <svg class="contact-icon" viewBox="0 0 20 20"><circle cx="10" cy="10" r="10" fill="var(--navy)"/><g stroke="#fff" stroke-width="1.1" fill="none"><circle cx="10" cy="10" r="5.5"/><ellipse cx="10" cy="10" rx="2.4" ry="5.5"/><path d="M4.5 10h11M5.4 7h9.2M5.4 13h9.2"/></g></svg>
      <span class="contact-web">www.brightledger.com.au</span>
    </p>
  </address>
</main>
</body>
</html>
```